Carpentry and Building Business Card

I'm looking for a business card that is minimalistic and that incorporates the theme of my Velmi logo.
On one side I'd like the VELMI logo with my details on the other side.
Double sided with curved edges

Target Market(s)

Construction / renovation
Adults

Industry/Entity Type

Tradesman

Contact Information for Business Card

Logo on one side, details on the other

Colors

Designer to choose only greyscale colors for use in the design.

Requirements
Must have
• Niko Barlettis
VELMI CONSTRUCT
Carpentry & Building Services
0412385726
Velmiconstruct@brindlemail.com
Lic No. 618243D
Nice to have
• Fb and insta icons. @velmiconstruct
Should not have
• No hammer or tool icons please.

No address line.

```html
<!DOCTYPE html>
<html lang="en">
<head>
<meta charset="utf-8">
<title>Velmi Construct Business Card</title>
<link href="https://fonts.googleapis.com/css2?family=Oswald:wght@500&family=Figtree:wght@400;500&display=swap" rel="stylesheet">
<style>
  :root {
    --backdrop: #444444;
    --charcoal: #232323;
    --accent: #a6a6a6;
    --back-face: #8f8f8f;
    --paper: #ffffff;
  }
  * { margin: 0; padding: 0; box-sizing: border-box; }
  html, body {
    width: 1125px;
    height: 1200px;
    overflow: hidden;
    background: var(--backdrop);
    font-family: "Figtree", sans-serif;
  }
  .card {
    position: absolute;
    left: 150px;
    width: 825px;
    height: 472px;
    overflow: hidden;
    border-radius: 14px;
  }
  .card--front { top: 106px; background: var(--paper); }
  .card--back { top: 639px; background: var(--back-face); }

  .details-panel {
    position: absolute;
    left: 0; top: 0;
    width: 359px; height: 100%;
    background: var(--charcoal);
    color: var(--paper);
  }
  .holder-name {
    position: absolute;
    left: 42px; top: 142px;
    font-family: "Oswald", sans-serif;
    font-weight: 500;
    font-size: 30px;
    line-height: 1;
    color: var(--accent);
    text-transform: uppercase;
    letter-spacing: 0.2px;
  }
  .contact-list {
    position: absolute;
    left: 42px; top: 202px;
    list-style: none;
  }
  .contact-item {
    display: flex;
    align-items: center;
    height: 23.4px;
    font-size: 17px;
    line-height: 1;
    white-space: nowrap;
  }
  .contact-icon {
    width: 15px; height: 15px;
    margin-right: 11px;
    flex: none;
  }
  .licence {
    position: absolute;
    left: 42px; top: 304px;
    font-size: 17px;
    line-height: 1;
  }
  .brand-panel {
    position: absolute;
    left: 359px; top: 0;
    width: 466px; height: 100%;
  }
  .brand-lockup {
    position: absolute;
    left: 0; right: 0; top: 172px;
    display: flex;
    justify-content: center;
    align-items: center;
    gap: 20px;
  }
  .brand-square {
    width: 38px; height: 38px;
    border: 3px solid var(--accent);
  }
  .brand-wordmark {
    font-weight: 500;
    font-size: 40px;
    letter-spacing: 9px;
    color: var(--charcoal);
    line-height: 1;
  }
  .back-wordmark {
    position: absolute;
    left: 0; right: 0; top: 200px;
    text-align: center;
    font-weight: 500;
    font-size: 64px;
    letter-spacing: 14px;
    padding-left: 14px;
    color: var(--paper);
    line-height: 1;
  }
  .back-caption {
    position: absolute;
    left: 0; right: 0; top: 380px;
    text-align: center;
    color: var(--paper);
    font-size: 18px;
    line-height: 24px;
  }
</style>
</head>
<body>
  <section class="card card--front">
    <div class="details-panel">
      <h1 class="holder-name">Niko Barlettis</h1>
      <ul class="contact-list">
        <li class="contact-item">
          <svg class="contact-icon" viewBox="0 0 16 16" aria-hidden="true"><path fill="#a6a6a6" d="M3.6 1.2l2.3 2.6-1.3 1.9c.9 2 2.7 3.8 4.7 4.7l1.9-1.3 2.6 2.3-1.2 2.3C7.3 14.4 1.6 8.7 1.3 2.4z"/></svg>
          041-238-5726
        </li>
        <li class="contact-item">
          <svg class="contact-icon" viewBox="0 0 16 16" aria-hidden="true"><rect x="1" y="3.5" width="14" height="9.5" fill="#a6a6a6"/><path d="M1.5 4l6.5 5 6.5-5" fill="none" stroke="#232323" stroke-width="1.3"/></svg>
          Velmiconstruct@brindlemail.com
        </li>
        <li class="contact-item">
          <svg class="contact-icon" viewBox="0 0 16 16" aria-hidden="true"><circle cx="8" cy="8" r="6.5" fill="none" stroke="#a6a6a6" stroke-width="1.6"/></svg>
          /velmiconstruct
        </li>
        <li class="contact-item">
          <svg class="contact-icon" viewBox="0 0 16 16" aria-hidden="true"><rect x="1.5" y="1.5" width="13" height="13" rx="3" fill="none" stroke="#a6a6a6" stroke-width="1.6"/></svg>
          @velmiconstruct
        </li>
      </ul>
      <p class="licence">LIC NO:&nbsp; 618243D</p>
    </div>
    <div class="brand-panel">
      <div class="brand-lockup">
        <span class="brand-square" aria-hidden="true"></span>
        <span class="brand-wordmark">VELMI.</span>
      </div>
    </div>
  </section>

  <section class="card card--back">
    <p class="back-wordmark">VELMI</p>
    <p class="back-caption">VELMI CONSTRUCT<br>Carpentry &amp; Building Services</p>
  </section>
</body>
</html>
```